Medical Billing - Professional Marketing Flier

We are needing help designing a clean and professional looking easy to read marketing flier for a medical billing practice. The text needs to be large enough to print. We are looking for a 5.5 x 8.5 design that we can edit the text as needed. I have included our logo and what we initially want it to say. Please keep in mind, we also want our logo and contact details on the flier. Let me know if you have any questions.

```html
<!DOCTYPE html>
<html lang="en">
<head>
<meta charset="utf-8">
<title>Lyra Medical Billing – Services Flier</title>
<link rel="stylesheet" href="https://fonts.googleapis.com/css2?family=Montserrat:wght@700&family=Questrial&display=swap">
<style>
  :root {
    --page-bg: #eef0f2;
    --paper: #ffffff;
    --ink: #2b2b2e;
    --band-light: #2fa3e0;
    --band-dark: #1d4c9e;
    --brand-purple: #7b52a6;
    --foot-light: #4fb0ec;
    --foot-pale: #bfe2f8;
    --helix-tint: #d9eef9;
    --white: #ffffff;
  }
  * { box-sizing: border-box; margin: 0; padding: 0; }
  html, body {
    width: 1200px; height: 1200px; overflow: hidden;
    background: var(--page-bg);
  }
  .flier {
    position: absolute; left: 246px; top: 52px;
    width: 708px; height: 1096px;
    background: var(--paper);
    overflow: hidden;
    font-family: "Questrial", sans-serif;
    color: var(--ink);
  }
  .helix-art {
    position: absolute; right: 0; top: 0;
    width: 420px; height: 720px;
    background:
      radial-gradient(ellipse at 75% 30%, var(--helix-tint) 0%, rgba(217,238,249,0.45) 40%, rgba(255,255,255,0) 75%);
  }
  .brand {
    position: absolute; left: 50px; top: 70px;
    display: flex; align-items: center; gap: 14px;
    color: var(--brand-purple);
    font-family: "Questrial", sans-serif;
  }
  .brand-dot {
    width: 18px; height: 18px; border-radius: 50%;
    background: var(--brand-purple);
  }
  .brand-name { font-size: 34px; letter-spacing: 2px; line-height: 1; }
  .brand-name small { display: block; font-size: 13px; letter-spacing: 4px; margin-top: 6px; }

  .section { position: absolute; left: 0; }
  .section-band {
    position: relative; height: 50px;
  }
  .section-band svg { position: absolute; left: 0; top: 0; }
  .section-title {
    position: absolute; left: 42px; top: 10px;
    font-family: "Montserrat", sans-serif; font-weight: 700;
    font-size: 28px; color: var(--white); letter-spacing: 0.5px;
  }
  .section-text {
    margin: 12px 0 0 42px; width: 548px;
    font-size: 13.6px; line-height: 17.5px;
  }
  .billing { top: 243px; }
  .aging { top: 460px; }
  .credentialing { top: 652px; }

  .footer-art { position: absolute; left: 0; top: 0; }
  .contact-title {
    position: absolute; left: 500px; top: 878px;
    font-family: "Montserrat", sans-serif; font-weight: 700;
    font-size: 23px; color: var(--white);
  }
  .footer-text {
    position: absolute; left: 42px; width: 620px;
    color: var(--white); font-size: 13px; line-height: 16.5px;
  }
  .footer-text.invite { top: 955px; }
  .footer-text.invite em { font-style: italic; font-weight: 700; }
  .footer-text.specialty { top: 1012px; font-size: 11.5px; line-height: 15px; }
</style>
</head>
<body>
  <article class="flier">
    <div class="helix-art" role="img" aria-label="Faint DNA double helix and chemical structure illustration"></div>

    <header class="brand">
      <span class="brand-dot"></span>
      <span class="brand-name">LYRA<small>MEDICAL BILLING</small></span>
    </header>

    <section class="section billing">
      <div class="section-band">
        <svg width="400" height="50" viewBox="0 0 400 50">
          <polygon points="0,0 340,0 308,50 0,50" fill="var(--band-light)"/>
          <polygon points="340,0 400,50 308,50" fill="var(--band-dark)"/>
        </svg>
        <h2 class="section-title">MEDICAL BILLING</h2>
      </div>
      <p class="section-text">Would you prefer to spend time focusing on your clients and running your practice rather than trying to stay up to speed with the constantly changing medical billing rules and regulations? Let us help you by managing your medical billing and dealing with the insurance companies on your behalf! We work with you to tailor the entire medical billing process to suit your practices needs while making it as smooth and painless as possible.</p>
    </section>

    <section class="section aging">
      <div class="section-band">
        <svg width="250" height="50" viewBox="0 0 250 50">
          <polygon points="0,0 190,0 158,50 0,50" fill="var(--band-light)"/>
          <polygon points="190,0 250,50 158,50" fill="var(--band-dark)"/>
        </svg>
        <h2 class="section-title">AGING</h2>
      </div>
      <p class="section-text">Are you leaving money on the table? Are you able to do the follow-through needed to keep your aging in check and more money flowing into your practice? Are you uncertain about how to get insurance to pay on claims that should be covered but for some reason they decided not to? We can clean up your aging, reduce the amount of time it takes for claims to pay out, and we can keep your aging to a minimum.</p>
    </section>

    <section class="section credentialing">
      <div class="section-band">
        <svg width="400" height="50" viewBox="0 0 400 50">
          <polygon points="0,0 340,0 308,50 0,50" fill="var(--band-light)"/>
          <polygon points="340,0 400,50 308,50" fill="var(--band-dark)"/>
        </svg>
        <h2 class="section-title">CREDENTIALING</h2>
      </div>
      <p class="section-text">Are you wanting to get contracted with insurance companies but aren't sure how to go about it? Are you wanting to expand your client base by having the option to bill insurance? Let us take the confusion out of what can seem like a daunting task! We can get you and your practitioners contracted with the insurance companies of your choice and help you navigate through the process every step of the way!</p>
    </section>

    <svg class="footer-art" width="708" height="1096" viewBox="0 0 708 1096">
      <defs>
        <linearGradient id="footGrad" x1="0" y1="0" x2="0" y2="1">
          <stop offset="0" stop-color="var(--foot-pale)"/>
          <stop offset="0.35" stop-color="var(--foot-light)"/>
          <stop offset="1" stop-color="var(--foot-light)"/>
        </linearGradient>
      </defs>
      <polygon points="0,912 708,860 708,1096 0,1096" fill="url(#footGrad)" role="img" aria-label="Blue band with faint DNA strand imagery"/>
      <polygon points="354,858 708,808 708,982" fill="var(--band-dark)"/>
    </svg>

    <h2 class="contact-title">CONTACT US</h2>
    <p class="footer-text invite">If any of these processes are something you would like our help with or to consult with us on, please <em>email us or give us a call!</em></p>
    <p class="footer-text specialty">We specialize in billing and contracting for Nutritionists and Dietitians. We would love to help you expand your business and take the pain and frustration out of billing so you can focus on your clients.</p>
  </article>
</body>
</html>
```